Book cover - Quiet Rooms, Open Doors

Book cover for Ebook (Pagelight) and wrap around print cover (Printvale) (back, front, and spine)

The book title (may slightly change by end of brief):
(MAIN TITLE) 'Quiet Rooms, Open Doors'
(SUB HEADING) 'A Week-by-Week Practical Workbook to Loosen Nervous Habits, Quieten Doubt and Build Steady Poise'
by Dr Owen Hartley

I would like a bold, stand out cover. Contemporary. I would like to avoid stereotypical images of people looking anxious or worried. I would like the design to be more uplifting and hopeful, rather than focusing on the negative aspect of anxiety, but avoiding cliched photos of people raising their hands in the air, smiling and jumping etc. The cover should appeal to both men and women.

Trim size of book cover (for PrintVale) is 5.25" x 8" back and front with a spine size of 0.477 inches

Reason: I have decided to extend the deadline by 1 more day, not because I am unhappy with the quality of the designs, but because a few designers have contacted me to explain they have had technical difficulties when submitting their files. Thanks everyone for the hard work and great designs.

Target Market(s)

Males and females (16+) who struggle with social anxiety and shyness

Industry/Entity Type

Social

Font styles to use
Serif

Requirements
Must have
• Bold cover that is modern and contemporary. For example, I like these covers:
• http://shrtlnk.example/k4Tq9Zb
• http://shrtlnk.example/m8Wv2Hn
• http://shrtlnk.example/p3Jx6Lr
• http://shrtlnk.example/t7Gd1Qe
• http://shrtlnk.example/v2Nk8Fy
• http://shrtlnk.example/w9Bh4Cs
• http://shrtlnk.example/z5Mf3Ud
Nice to have
• Open to abstract designs.
Should not have
• No stereotypical pictures of people who look anxious or worried. Avoid cliched photos of people raising their hands in the air, smiling and jumping etc.

```html
<!DOCTYPE html>
<html lang="en">
<head>
<meta charset="utf-8">
<title>Quiet Rooms, Open Doors — Front Cover</title>
<link href="https://fonts.googleapis.com/css2?family=Cinzel:wght@400;500&family=Quicksand:wght@400;500;700&display=swap" rel="stylesheet">
<style>
  :root {
    --page-bg: #ffffff;
    --cover-pink-left: #f28b8b;
    --cover-pink-mid: #f5a3ad;
    --cover-pink-right: #f7bccd;
    --snow-pink: #f7c4d6;
    --peak-coral: #f0604c;
    --peak-rose: #ee7a84;
    --peak-lavender: #a6a5cc;
    --peak-blue: #93bde2;
    --ink-light: #fdf3f3;
    --ink-shadow: rgba(150, 60, 70, 0.35);
  }

  * { margin: 0; padding: 0; box-sizing: border-box; }

  html, body {
    width: 1200px;
    height: 1200px;
    overflow: hidden;
    background: var(--page-bg);
  }

  .canvas {
    width: 1200px;
    height: 1200px;
    display: flex;
    align-items: center;
    justify-content: center;
  }

  .front-cover {
    position: relative;
    width: 736px;
    height: 1120px;
    overflow: hidden;
    background: linear-gradient(100deg,
      var(--cover-pink-left) 0%,
      var(--cover-pink-mid) 55%,
      var(--cover-pink-right) 100%);
    color: var(--ink-light);
    text-align: center;
  }

  .book-title {
    position: absolute;
    top: 80px;
    left: 0;
    right: 0;
    font-family: "Cinzel", serif;
    font-weight: 400;
    line-height: 1.12;
    text-shadow: 0 2px 3px var(--ink-shadow);
  }

  .book-title .title-lead {
    display: block;
    font-size: 54px;
    letter-spacing: 3px;
  }

  .book-title .title-main {
    display: block;
    font-size: 76px;
    font-weight: 500;
    letter-spacing: 2px;
    margin-top: 14px;
  }

  .subtitle {
    position: absolute;
    top: 362px;
    left: 70px;
    right: 70px;
    font-family: "Quicksand", sans-serif;
    font-size: 22px;
    line-height: 1.4;
    text-shadow: 0 1px 2px var(--ink-shadow);
  }

  .subtitle .subtitle-lead {
    display: block;
    font-weight: 700;
    font-size: 23px;
  }

  .subtitle .subtitle-rest {
    font-weight: 400;
  }

  .landscape-art {
    position: absolute;
    left: 0;
    right: 0;
    top: 470px;
    height: 520px;
    background:
      linear-gradient(180deg, rgba(247, 196, 214, 0) 0%, rgba(247, 196, 214, 0) 75%, var(--snow-pink) 100%),
      linear-gradient(100deg,
        var(--peak-coral) 0%,
        var(--peak-lavender) 30%,
        var(--peak-coral) 45%,
        var(--peak-blue) 62%,
        var(--peak-rose) 80%,
        var(--peak-blue) 100%);
    -webkit-mask-image: linear-gradient(180deg, transparent 0%, #000 22%, #000 78%, transparent 100%);
    mask-image: linear-gradient(180deg, transparent 0%, #000 22%, #000 78%, transparent 100%);
  }

  .author {
    position: absolute;
    top: 1000px;
    left: 0;
    right: 0;
    font-family: "Quicksand", sans-serif;
    font-weight: 500;
    font-size: 38px;
    letter-spacing: 1px;
    text-shadow: 0 2px 3px var(--ink-shadow);
  }
</style>
</head>
<body>
  <main class="canvas">
    <section class="front-cover">
      <h1 class="book-title">
        <span class="title-lead">QUIET ROOMS,</span>
        <span class="title-main">OPEN DOORS</span>
      </h1>

      <p class="subtitle">
        <span class="subtitle-lead">A Week-by-Week Practical Workbook</span>
        <span class="subtitle-rest">to Loosen Nervous Habits, Quieten Doubt and Build Steady Poise</span>
      </p>

      <div class="landscape-art" role="img" aria-label="Abstract low-poly mountain range in coral, lavender and pale blue rising from soft pink ground"></div>

      <p class="author">by Dr Owen Hartley</p>
    </section>
  </main>
</body>
</html>
```